Quarrydeen Fintech Product Infographic

Quarrydeen is an established Fintech business, supplying complex financial software to banks and building societies.

We currently have a picture/infographic to show each of our 11 different software products in a single image. Each product can be installed on its own as a standalone application or if multiple products are installed they will share data.

The key message for our infographic is to convey the integration via a shared database.

The attached diagram is what we currently use which is to give you an idea of the message we are trying to give, but we are not tied to this format and are looking for this diagram to be reimagined.

We will look to use our new chosen design on printed media such as A4 Data sheets an example of which is attached.

For more information on our products please refer to www.quarrydeen.co.uk/products

```html
<!DOCTYPE html>
<html lang="en">
<head>
<meta charset="utf-8">
<title>Quarrydeen Fintech Product Infographic</title>
<link rel="stylesheet" href="https://fonts.googleapis.com/css2?family=Oswald:wght@500;600&family=Nunito+Sans:wght@600&display=swap">
<style>
  :root {
    --bg: #ffffff;
    --ink: #676767;
    --heading: #6a6a6a;
    --performance: #b87db6;
    --performance-soft: #d9b4d8;
    --finance: #6ccbec;
    --finance-soft: #b3e3f4;
    --risk: #f9b94f;
    --risk-soft: #fbd596;
    --regulatory: #5fbf8b;
    --regulatory-soft: #a6dcbd;
  }
  html, body {
    margin: 0;
    padding: 0;
    width: 1200px;
    height: 1200px;
    overflow: hidden;
    background: var(--bg);
  }
  .infographic { display: block; width: 1200px; height: 1200px; }
  .group-title {
    font-family: "Oswald", "Arial Narrow", sans-serif;
    font-weight: 500;
    font-size: 36px;
    fill: var(--heading);
    text-anchor: middle;
    letter-spacing: 0.5px;
  }
  .hub-label {
    font-family: "Oswald", "Arial Narrow", sans-serif;
    font-weight: 600;
    font-size: 56px;
    fill: var(--heading);
    text-anchor: middle;
    letter-spacing: 1px;
  }
  .product {
    font-family: "Nunito Sans", "Helvetica", sans-serif;
    font-weight: 600;
    font-size: 27px;
    fill: var(--ink);
    text-anchor: middle;
  }
  .ring { fill: none; stroke-width: 10; }
  .divider { stroke-width: 3; }
  .performance .ring { stroke: var(--performance); }
  .performance .divider { stroke: var(--performance-soft); }
  .finance .ring { stroke: var(--finance); }
  .finance .divider { stroke: var(--finance-soft); }
  .risk .ring { stroke: var(--risk); }
  .risk .divider { stroke: var(--risk-soft); }
  .regulatory .ring { stroke: var(--regulatory); }
  .regulatory .divider { stroke: var(--regulatory-soft); }
</style>
</head>
<body>
<svg class="infographic" viewBox="0 0 1200 1200" xmlns="http://www.w3.org/2000/svg" role="img" aria-label="Quarrydeen products grouped in four areas around shared data">
  <defs>
    <path id="lobe" d="M573 463.7 A182 182 0 1 0 469.2 565.9 A140 140 0 0 1 573 463.7 Z"/>
  </defs>

  <g class="performance">
    <use href="#lobe" class="ring"/>
    <line class="divider" x1="228" y1="355" x2="580" y2="355"/>
    <line class="divider" x1="229" y1="442" x2="579" y2="442"/>
    <text class="group-title" x="398" y="182">PERFORMANCE</text>
    <text class="product" x="398" y="298">Financial</text>
    <text class="product" x="398" y="333">Planning</text>
    <text class="product" x="398" y="389">Funds Transfer</text>
    <text class="product" x="398" y="424">Pricing</text>
    <text class="product" x="398" y="478">Business</text>
    <text class="product" x="398" y="513">Intelligence</text>
  </g>

  <g class="finance">
    <use href="#lobe" class="ring" transform="translate(1210 0) scale(-1 1)"/>
    <line class="divider" x1="630" y1="355" x2="982" y2="355"/>
    <line class="divider" x1="631" y1="442" x2="981" y2="442"/>
    <text class="group-title" x="806" y="182">FINANCE</text>
    <text class="product" x="813" y="298">Financial</text>
    <text class="product" x="813" y="333">Ledgers</text>
    <text class="product" x="813" y="389">Effective Interest</text>
    <text class="product" x="813" y="424">Rates</text>
    <text class="product" x="813" y="478">Hedges</text>
    <text class="product" x="813" y="513">Accounting</text>
  </g>

  <g class="risk">
    <use href="#lobe" class="ring" transform="translate(0 1200) scale(1 -1)"/>
    <line class="divider" x1="223" y1="804" x2="585" y2="804"/>
    <text class="group-title" x="398" y="1044">RISK</text>
    <text class="product" x="398" y="758">Treasury</text>
    <text class="product" x="398" y="858">ALM</text>
  </g>

  <g class="regulatory">
    <use href="#lobe" class="ring" transform="translate(1210 1200) scale(-1 -1)"/>
    <line class="divider" x1="631" y1="760" x2="981" y2="760"/>
    <line class="divider" x1="630" y1="847" x2="982" y2="847"/>
    <text class="group-title" x="807" y="1044">REGULATORY</text>
    <text class="product" x="813" y="707">Regulatory</text>
    <text class="product" x="813" y="742">Reporting</text>
    <text class="product" x="813" y="798">Taxation</text>
    <text class="product" x="813" y="833">Reporting</text>
    <text class="product" x="813" y="905">DGSR SCV</text>
  </g>

  <g class="hub">
    <text class="hub-label" x="605" y="598">SHARED</text>
    <text class="hub-label" x="605" y="654">DATA</text>
  </g>
</svg>
</body>
</html>
```